TAILORFLOW User Interface

I need a new design for our TAILORFLOW screens. They need to be end user friendly and contain the data in an easy to read format. These are online orders. I have attached 3 images from the development solution. For now I just need a new UI and ideally would like it delivered in html so we can easily adapt. The screen has multiple tabs to display the different types of data we store. Ideally the end user needs to see customer focused information first.
I have uploaded an example of a different order view that i like.
Industry/Entity Type
Fashion Retail
Coding
Coded - Design and coding required
Number of Pages Required
1 page

```html
<!DOCTYPE html>
<html lang="en">
<head>
<meta charset="utf-8">
<title>Tailorflow – Order Screens</title>
<link href="https://fonts.googleapis.com/css2?family=Roboto:wght@400;500;700&display=swap" rel="stylesheet">
<style>
:root{
  --page:#e8eaed;
  --navy:#22408d;
  --sky:#79b5c9;
  --content:#edf0f3;
  --field:#f3f4f6;
  --field-line:#e1e4e8;
  --ink:#2b2b2b;
  --muted:#6b6f75;
  --footer:#232323;
  --grid:#e4e6ea;
}
*{box-sizing:border-box;margin:0;padding:0}
html,body{width:1200px;height:3686px;overflow:hidden}
body{background:var(--page);font-family:'Roboto',sans-serif;color:var(--ink);position:relative}
.card{position:absolute;left:67px;width:1066px;background:#fff;border-radius:10px;box-shadow:0 2px 10px rgba(0,0,0,.18)}
.screen{position:absolute;left:77px;width:1047px;overflow:hidden;background:var(--content)}
.topbar{position:absolute;left:0;top:0;right:0;height:73px;background:#fff}
.brand{position:absolute;left:0;top:0;width:232px;height:73px;display:flex;align-items:center;justify-content:center;gap:9px;color:var(--navy);font-weight:700;font-size:19px;letter-spacing:.5px}
.brand-mark{width:14px;height:14px;background:var(--sky);flex:none}
.tab{position:absolute;top:11px;height:42px;font-size:12px;font-weight:700;display:flex;align-items:center;justify-content:center;letter-spacing:.3px}
.tab-search{left:267px;width:141px;border:2px solid var(--sky);color:var(--navy);background:#fff}
.tab-order{left:419px;width:143px;background:var(--sky);color:#fff;box-shadow:0 2px 5px rgba(0,0,0,.25)}
.avatar{position:absolute;left:885px;top:14px;width:38px;height:38px;border-radius:50%;background:linear-gradient(135deg,#9aa3ab,#5c646c)}
.username{position:absolute;left:934px;top:25px;font-size:12.5px;font-weight:500;color:#222}
.user-caret{position:absolute;left:1010px;top:28px}
.sidebar{position:absolute;left:0;top:73px;width:232px;bottom:77px;background:var(--navy)}
.nav{position:absolute;left:0;top:39px;width:232px;list-style:none}
.nav li{height:44px;display:flex;align-items:center;color:#fff;font-size:13.5px;font-weight:500}
.nav li.active{background:var(--sky)}
.nav svg{margin-left:26px;margin-right:20px;width:16px;height:16px;flex:none}
.footer{position:absolute;left:0;right:0;bottom:0;height:77px;background:var(--footer);color:#fff;font-size:11.5px;display:flex;align-items:center;justify-content:center}
.footer b{font-weight:700;margin:0 4px}
.footer .code{position:absolute;right:26px;font-size:10px}
.panel{position:absolute;left:267px;width:753px;background:#fff;box-shadow:0 1px 3px rgba(0,0,0,.06)}
.order-form{top:104px;height:344px}
.lbl{position:absolute;font-size:11.5px;color:#222;line-height:31px}
.fld{position:absolute;height:31px;background:var(--field);border:1px solid var(--field-line);font-size:10px;color:var(--muted);line-height:29px;padding-left:9px}
.spin{position:absolute;right:6px;top:10px;width:6px;height:10px}
.check{position:absolute;left:218px;top:286px;width:11px;height:11px;border:1px solid var(--sky)}
.check-lbl{position:absolute;left:238px;top:283px;font-size:11.5px}
.btn{position:absolute;height:37px;width:91px;font-size:11.5px;font-weight:700;display:flex;align-items:center;justify-content:center}
.btn-outline{border:2px solid var(--sky);color:var(--navy);background:#fff}
.btn-fill{background:var(--sky);color:#fff}
.select{position:absolute;left:32px;width:689px;height:38px;border:2px solid var(--sky);font-size:11px;color:var(--navy);font-weight:500;padding-left:13px;line-height:34px}
.select svg{position:absolute;right:10px;top:13px}
.tray{position:absolute;left:32px;width:689px;background:#e9ebee}
.tbl-wrap{position:absolute;left:14px;width:645px;overflow:hidden;background:#fff}
table{border-collapse:collapse;table-layout:fixed;width:645px}
th{background:var(--navy);color:#fff;font-weight:500;font-size:10.5px;line-height:14px}
td{font-size:10.5px;color:#333;text-align:center;border-right:1px solid var(--grid);border-bottom:1px solid var(--grid)}
.items th{height:55px}
.items td{height:228px}
.sub{width:100%;border-collapse:collapse}
.sub td{height:38px;border-bottom:1px solid var(--grid);border-right:1px solid var(--grid);font-size:10.5px;color:#444}
.sub td:last-child{border-right:0}
.items td.prod{padding:0;vertical-align:top}
.sku{color:var(--navy);font-weight:500}
.addr th{height:51px;font-size:11px}
.addr td{height:64px;font-size:10px;color:#444}
.addr tr:nth-child(odd) td{background:#f2f3f5}
.addr .edit{color:var(--sky);font-weight:500}
.scroll{position:absolute;width:11px;background:#d9dce0}
.scroll i{position:absolute;left:1px;width:9px;height:9px;background:#9fc3d2}
.shade{position:absolute;inset:0;background:rgba(0,0,0,.62)}
.modal{position:absolute;left:97px;top:177px;width:851px;height:773px;background:#fff}
.modal-head{position:absolute;left:4px;top:4px;right:4px;height:50px;background:var(--sky);color:#fff;font-size:16px;font-weight:700;letter-spacing:1px;display:flex;align-items:center;justify-content:center}
.modal-head svg{position:absolute;right:12px;top:17px}
.mlbl{position:absolute;font-size:12px;color:#222}
.mfld{position:absolute;height:37px;background:var(--field);border:1px solid var(--field-line);font-size:11px;color:var(--muted);line-height:35px;padding-left:18px}
</style>
</head>
<body>

<!-- ============ Screen 1 : Items ============ -->
<div class="card" style="top:79px;height:1094px"></div>
<section class="screen" style="top:89px;height:1075px">
  <header class="topbar">
    <div class="brand"><span class="brand-mark"></span>TAILORFLOW</div>
    <div class="tab tab-search">ORDER SEARCH</div>
    <div class="tab tab-order">ORDER 9670363</div>
    <div class="avatar" role="img" aria-label="User profile photo"></div>
    <div class="username">John Doe</div>
    <svg class="user-caret" width="10" height="6" viewBox="0 0 10 6"><path d="M1 1l4 4 4-4" fill="none" stroke="#333" stroke-width="1.5"/></svg>
  </header>
  <aside class="sidebar">
    <ul class="nav">
      <li class="active"><svg viewBox="0 0 16 16"><rect x="1" y="2" width="14" height="9" fill="#fff"/><rect x="5" y="12" width="6" height="2" fill="#fff"/></svg>Development</li>
      <li><svg viewBox="0 0 16 16"><path d="M1 2h3l2 8h8l1.5-6H5" fill="none" stroke="#fff" stroke-width="1.8"/><circle cx="7" cy="13.5" r="1.4" fill="#fff"/><circle cx="13" cy="13.5" r="1.4" fill="#fff"/></svg>Purchase</li>
      <li><svg viewBox="0 0 16 16"><rect x="1" y="3" width="14" height="2.5" fill="#fff"/><rect x="1" y="7" width="14" height="2.5" fill="#fff"/><rect x="1" y="11" width="14" height="2.5" fill="#fff"/></svg>Product</li>
      <li><svg viewBox="0 0 16 16"><path d="M8 1a4.5 4.5 0 0 0-4.5 4.5C3.5 9 8 15 8 15s4.5-6 4.5-9.5A4.5 4.5 0 0 0 8 1z" fill="#fff"/><circle cx="8" cy="5.5" r="1.7" fill="#22408d"/></svg>Location</li>
      <li><svg viewBox="0 0 16 16"><circle cx="5" cy="5" r="2.5" fill="#fff"/><circle cx="11" cy="5" r="2.5" fill="#fff"/><path d="M0 14c0-3 2-5 5-5s5 2 5 5zM7 14c0-3 1.5-5 4-5s5 2 5 5z" fill="#fff"/></svg>Customer</li>
      <li><svg viewBox="0 0 16 16"><path d="M1 8s3-5 7-5 7 5 7 5-3 5-7 5-7-5-7-5z" fill="#fff"/><circle cx="8" cy="8" r="2.2" fill="#22408d"/></svg>View Order List</li>
      <li><svg viewBox="0 0 16 16"><circle cx="8" cy="8" r="6.5" fill="none" stroke="#fff" stroke-width="1.6"/><circle cx="8" cy="6.5" r="2.2" fill="#fff"/><path d="M4 12.5c1-2 2.4-2.8 4-2.8s3 .8 4 2.8" fill="#fff"/></svg>User</li>
    </ul>
  </aside>

  <div class="panel order-form">
    <span class="lbl" style="left:32px;top:35px">Order No</span><span class="fld" style="left:125px;top:35px;width:126px">9670363</span>
    <span class="lbl" style="left:268px;top:35px">Reference</span><span class="fld" style="left:361px;top:35px;width:124px">9670363</span>
    <span class="lbl" style="left:504px;top:35px">Surname</span><span class="fld" style="left:595px;top:35px;width:126px">Order</span>
    <span class="lbl" style="left:32px;top:74px">Orig Order No</span><span class="fld" style="left:125px;top:74px;width:126px">9670363</span>
    <span class="lbl" style="left:268px;top:74px">Firstname</span><span class="fld" style="left:361px;top:74px;width:124px">Test</span>
    <span class="lbl" style="left:504px;top:74px">Shipping</span><span class="fld" style="left:595px;top:74px;width:126px">0<svg class="spin" viewBox="0 0 6 10"><path d="M0 4l3-3 3 3zM0 6l3 3 3-3z" fill="#79b5c9"/></svg></span>
    <span class="lbl" style="left:32px;top:113px">Customer No</span><span class="fld" style="left:125px;top:113px;width:126px"></span>
    <span class="lbl" style="left:268px;top:113px">Total tax</span><span class="fld" style="left:361px;top:113px;width:124px">9.55<svg class="spin" viewBox="0 0 6 10"><path d="M0 4l3-3 3 3zM0 6l3 3 3-3z" fill="#79b5c9"/></svg></span>
    <span class="lbl" style="left:504px;top:113px">Delivey</span><span class="fld" style="left:595px;top:113px;width:126px">0<svg class="spin" viewBox="0 0 6 10"><path d="M0 4l3-3 3 3zM0 6l3 3 3-3z" fill="#79b5c9"/></svg></span>
    <span class="lbl" style="left:32px;top:151px">Total Retail</span><span class="fld" style="left:125px;top:151px;width:126px">105<svg class="spin" viewBox="0 0 6 10"><path d="M0 4l3-3 3 3zM0 6l3 3 3-3z" fill="#79b5c9"/></svg></span>
    <span class="lbl" style="left:268px;top:151px">Order Type</span><span class="fld" style="left:361px;top:151px;width:124px">Sale</span>
    <span class="lbl" style="left:504px;top:151px">Customer email</span><span class="fld" style="left:595px;top:151px;width:126px"></span>
    <span class="lbl" style="left:32px;top:190px">Brand</span><span class="fld" style="left:125px;top:190px;width:126px"></span>
    <span class="lbl" style="left:268px;top:190px">Oreder Channel</span><span class="fld" style="left:361px;top:190px;width:124px">Standard</span>
    <span class="lbl" style="left:504px;top:190px">Shippong Tax</span><span class="fld" style="left:595px;top:190px;width:126px">0<svg class="spin" viewBox="0 0 6 10"><path d="M0 4l3-3 3 3zM0 6l3 3 3-3z" fill="#79b5c9"/></svg></span>
    <span class="lbl" style="left:32px;top:228px">Instructions</span><span class="fld" style="left:125px;top:228px;width:360px"></span>
    <span class="lbl" style="left:504px;top:228px">Created</span><span class="fld" style="left:595px;top:228px;width:126px">21/01/2022&nbsp; 02.55pm</span>
    <svg class="check" viewBox="0 0 11 11"><path d="M2 5.5l2.5 2.5L9 3" fill="none" stroke="#79b5c9" stroke-width="1.3"/></svg>
    <span class="check-lbl">Autority To Leave</span>
    <div class="btn btn-outline" style="left:351px;top:274px">SAVE</div>
    <div class="btn btn-fill" style="left:448px;top:274px">REFRESH</div>
  </div>

  <div class="panel" style="top:480px;height:457px">
    <div class="select" style="top:35px">Items<svg width="10" height="6" viewBox="0 0 10 6"><path d="M1 1l4 4 4-4" fill="none" stroke="#79b5c9" stroke-width="1.3"/></svg></div>
    <div class="tray" style="top:92px;height:337px">
      <div class="tbl-wrap" style="top:29px;height:280px">
        <table class="items">
          <colgroup><col style="width:37px"><col style="width:59px"><col style="width:156px"><col style="width:69px"><col style="width:47px"><col style="width:37px"><col style="width:56px"><col style="width:36px"><col style="width:59px"><col style="width:53px"><col style="width:36px"></colgroup>
          <thead><tr><th>S.No</th><th>SKU</th><th>Product</th><th>Is Drop</th><th>Quantity</th><th>Unit</th><th>Discount</th><th>Final</th><th>Discount Reason</th><th>Coupon Code</th><th>Status</th></tr></thead>
          <tbody><tr>
            <td>1</td><td class="sku">2230556</td>
            <td class="prod"><table class="sub"><colgroup><col style="width:90px"><col></colgroup>
              <tr><td>Vendor</td><td></td></tr>
              <tr><td>Brand</td><td></td></tr>
              <tr><td>Product Code</td><td>2002539</td></tr>
              <tr><td>Description</td><td>PJ SET</td></tr>
              <tr><td>Colour (Code)</td><td>900</td></tr>
              <tr><td>Size</td><td>12/14</td></tr>
            </table></td>
            <td>False</td><td>1</td><td>35.00</td><td>0.00</td><td>35.00</td><td></td><td></td><td></td>
          </tr></tbody>
        </table>
      </div>
      <div class="scroll" style="left:665px;top:87px;height:222px"><i style="top:1px"></i><i style="bottom:1px"></i></div>
    </div>
  </div>

  <footer class="footer">© 2022 <b>TAILORFLOW</b> | &nbsp;All Rights Reserved<span class="code">C45</span></footer>
</section>

<!-- ============ Screen 2 : Addresses ============ -->
<div class="card" style="top:1238px;height:1150px"></div>
<section class="screen" style="top:1248px;height:1131px">
  <header class="topbar">
    <div class="brand"><span class="brand-mark"></span>TAILORFLOW</div>
    <div class="tab tab-search">ORDER SEARCH</div>
    <div class="tab tab-order">ORDER 9670363</div>
    <div class="avatar" role="img" aria-label="User profile photo"></div>
    <div class="username">John Doe</div>
    <svg class="user-caret" width="10" height="6" viewBox="0 0 10 6"><path d="M1 1l4 4 4-4" fill="none" stroke="#333" stroke-width="1.5"/></svg>
  </header>
  <aside class="sidebar">
    <ul class="nav">
      <li class="active"><svg viewBox="0 0 16 16"><rect x="1" y="2" width="14" height="9" fill="#fff"/><rect x="5" y="12" width="6" height="2" fill="#fff"/></svg>Development</li>
      <li><svg viewBox="0 0 16 16"><path d="M1 2h3l2 8h8l1.5-6H5" fill="none" stroke="#fff" stroke-width="1.8"/><circle cx="7" cy="13.5" r="1.4" fill="#fff"/><circle cx="13" cy="13.5" r="1.4" fill="#fff"/></svg>Purchase</li>
      <li><svg viewBox="0 0 16 16"><rect x="1" y="3" width="14" height="2.5" fill="#fff"/><rect x="1" y="7" width="14" height="2.5" fill="#fff"/><rect x="1" y="11" width="14" height="2.5" fill="#fff"/></svg>Product</li>
      <li><svg viewBox="0 0 16 16"><path d="M8 1a4.5 4.5 0 0 0-4.5 4.5C3.5 9 8 15 8 15s4.5-6 4.5-9.5A4.5 4.5 0 0 0 8 1z" fill="#fff"/><circle cx="8" cy="5.5" r="1.7" fill="#22408d"/></svg>Location</li>
      <li><svg viewBox="0 0 16 16"><circle cx="5" cy="5" r="2.5" fill="#fff"/><circle cx="11" cy="5" r="2.5" fill="#fff"/><path d="M0 14c0-3 2-5 5-5s5 2 5 5zM7 14c0-3 1.5-5 4-5s5 2 5 5z" fill="#fff"/></svg>Customer</li>
      <li><svg viewBox="0 0 16 16"><path d="M1 8s3-5 7-5 7 5 7 5-3 5-7 5-7-5-7-5z" fill="#fff"/><circle cx="8" cy="8" r="2.2" fill="#22408d"/></svg>View Order List</li>
      <li><svg viewBox="0 0 16 16"><circle cx="8" cy="8" r="6.5" fill="none" stroke="#fff" stroke-width="1.6"/><circle cx="8" cy="6.5" r="2.2" fill="#fff"/><path d="M4 12.5c1-2 2.4-2.8 4-2.8s3 .8 4 2.8" fill="#fff"/></svg>User</li>
    </ul>
  </aside>

  <div class="panel order-form">
    <span class="lbl" style="left:32px;top:35px">Order No</span><span class="fld" style="left:125px;top:35px;width:126px">9670363</span>
    <span class="lbl" style="left:268px;top:35px">Reference</span><span class="fld" style="left:361px;top:35px;width:124px">9670363</span>
    <span class="lbl" style="left:504px;top:35px">Surname</span><span class="fld" style="left:595px;top:35px;width:126px">Order</span>
    <span class="lbl" style="left:32px;top:74px">Orig Order No</span><span class="fld" style="left:125px;top:74px;width:126px">9670363</span>
    <span class="lbl" style="left:268px;top:74px">Firstname</span><span class="fld" style="left:361px;top:74px;width:124px">Test</span>
    <span class="lbl" style="left:504px;top:74px">Shipping</span><span class="fld" style="left:595px;top:74px;width:126px">0<svg class="spin" viewBox="0 0 6 10"><path d="M0 4l3-3 3 3zM0 6l3 3 3-3z" fill="#79b5c9"/></svg></span>
    <span class="lbl" style="left:32px;top:113px">Customer No</span><span class="fld" style="left:125px;top:113px;width:126px"></span>
    <span class="lbl" style="left:268px;top:113px">Total tax</span><span class="fld" style="left:361px;top:113px;width:124px">9.55<svg class="spin" viewBox="0 0 6 10"><path d="M0 4l3-3 3 3zM0 6l3 3 3-3z" fill="#79b5c9"/></svg></span>
    <span class="lbl" style="left:504px;top:113px">Delivey</span><span class="fld" style="left:595px;top:113px;width:126px">0<svg class="spin" viewBox="0 0 6 10"><path d="M0 4l3-3 3 3zM0 6l3 3 3-3z" fill="#79b5c9"/></svg></span>
    <span class="lbl" style="left:32px;top:151px">Total Retail</span><span class="fld" style="left:125px;top:151px;width:126px">105<svg class="spin" viewBox="0 0 6 10"><path d="M0 4l3-3 3 3zM0 6l3 3 3-3z" fill="#79b5c9"/></svg></span>
    <span class="lbl" style="left:268px;top:151px">Order Type</span><span class="fld" style="left:361px;top:151px;width:124px">Sale</span>
    <span class="lbl" style="left:504px;top:151px">Customer email</span><span class="fld" style="left:595px;top:151px;width:126px"></span>
    <span class="lbl" style="left:32px;top:190px">Brand</span><span class="fld" style="left:125px;top:190px;width:126px"></span>
    <span class="lbl" style="left:268px;top:190px">Oreder Channel</span><span class="fld" style="left:361px;top:190px;width:124px">Standard</span>
    <span class="lbl" style="left:504px;top:190px">Shippong Tax</span><span class="fld" style="left:595px;top:190px;width:126px">0<svg class="spin" viewBox="0 0 6 10"><path d="M0 4l3-3 3 3zM0 6l3 3 3-3z" fill="#79b5c9"/></svg></span>
    <span class="lbl" style="left:32px;top:228px">Instructions</span><span class="fld" style="left:125px;top:228px;width:360px"></span>
    <span class="lbl" style="left:504px;top:228px">Created</span><span class="fld" style="left:595px;top:228px;width:126px">21/01/2022&nbsp; 02.55pm</span>
    <svg class="check" viewBox="0 0 11 11"><path d="M2 5.5l2.5 2.5L9 3" fill="none" stroke="#79b5c9" stroke-width="1.3"/></svg>
    <span class="check-lbl">Autority To Leave</span>
    <div class="btn btn-outline" style="left:351px;top:274px">SAVE</div>
    <div class="btn btn-fill" style="left:448px;top:274px">REFRESH</div>
  </div>

  <div class="panel" style="top:480px;height:508px">
    <div class="select" style="top:43px">Addresses<svg width="10" height="6" viewBox="0 0 10 6"><path d="M1 1l4 4 4-4" fill="none" stroke="#79b5c9" stroke-width="1.3"/></svg></div>
    <div class="tray" style="top:99px;height:363px">
      <div class="tbl-wrap" style="top:29px;height:307px">
        <table class="addr">
          <colgroup><col style="width:57px"><col style="width:84px"><col style="width:109px"><col style="width:116px"><col style="width:103px"><col style="width:109px"><col style="width:67px"></colgroup>
          <thead><tr><th>Type</th><th>Name</th><th>Attention Of</th><th>Address</th><th>Email</th><th>Phone</th><th>Actions</th></tr></thead>
          <tbody>
            <tr><td>Delivery</td><td>Test Order</td><td></td><td>465, Lorum Ipsum<br>United States</td><td></td><td>+1 (888) 888 8888</td><td class="edit">EDIT</td></tr>
            <tr><td>Postal</td><td>Test Order</td><td></td><td>465, Lorum Ipsum<br>United States</td><td></td><td>+1 (888) 888 8888</td><td class="edit">EDIT</td></tr>
            <tr><td>Delivery</td><td>Test Order</td><td></td><td>465, Lorum Ipsum<br>United States</td><td></td><td>+1 (888) 888 8888</td><td class="edit">EDIT</td></tr>
            <tr><td>Postal</td><td>Test Order</td><td></td><td>465, Lorum Ipsum<br>United States</td><td></td><td>+1 (888) 888 8888</td><td class="edit">EDIT</td></tr>
          </tbody>
        </table>
      </div>
      <div class="scroll" style="left:665px;top:80px;height:256px"><i style="top:1px"></i><i style="bottom:1px"></i></div>
    </div>
  </div>

  <footer class="footer">© 2022 <b>TAILORFLOW</b> | &nbsp;All Rights Reserved<span class="code">C45</span></footer>
</section>

<!-- ============ Screen 3 : Edit address dialog ============ -->
<div class="card" style="top:2455px;height:1151px"></div>
<section class="screen" style="top:2465px;height:1131px">
  <header class="topbar">
    <div class="brand"><span class="brand-mark"></span>TAILORFLOW</div>
    <div class="tab tab-search">ORDER SEARCH</div>
    <div class="tab tab-order">ORDER 9670363</div>
    <div class="avatar" role="img" aria-label="User profile photo"></div>
    <div class="username">John Doe</div>
    <svg class="user-caret" width="10" height="6" viewBox="0 0 10 6"><path d="M1 1l4 4 4-4" fill="none" stroke="#333" stroke-width="1.5"/></svg>
  </header>
  <aside class="sidebar">
    <ul class="nav">
      <li class="active"><svg viewBox="0 0 16 16"><rect x="1" y="2" width="14" height="9" fill="#fff"/><rect x="5" y="12" width="6" height="2" fill="#fff"/></svg>Development</li>
      <li><svg viewBox="0 0 16 16"><path d="M1 2h3l2 8h8l1.5-6H5" fill="none" stroke="#fff" stroke-width="1.8"/><circle cx="7" cy="13.5" r="1.4" fill="#fff"/><circle cx="13" cy="13.5" r="1.4" fill="#fff"/></svg>Purchase</li>
      <li><svg viewBox="0 0 16 16"><rect x="1" y="3" width="14" height="2.5" fill="#fff"/><rect x="1" y="7" width="14" height="2.5" fill="#fff"/><rect x="1" y="11" width="14" height="2.5" fill="#fff"/></svg>Product</li>
      <li><svg viewBox="0 0 16 16"><path d="M8 1a4.5 4.5 0 0 0-4.5 4.5C3.5 9 8 15 8 15s4.5-6 4.5-9.5A4.5 4.5 0 0 0 8 1z" fill="#fff"/><circle cx="8" cy="5.5" r="1.7" fill="#22408d"/></svg>Location</li>
      <li><svg viewBox="0 0 16 16"><circle cx="5" cy="5" r="2.5" fill="#fff"/><circle cx="11" cy="5" r="2.5" fill="#fff"/><path d="M0 14c0-3 2-5 5-5s5 2 5 5zM7 14c0-3 1.5-5 4-5s5 2 5 5z" fill="#fff"/></svg>Customer</li>
      <li><svg viewBox="0 0 16 16"><path d="M1 8s3-5 7-5 7 5 7 5-3 5-7 5-7-5-7-5z" fill="#fff"/><circle cx="8" cy="8" r="2.2" fill="#22408d"/></svg>View Order List</li>
      <li><svg viewBox="0 0 16 16"><circle cx="8" cy="8" r="6.5" fill="none" stroke="#fff" stroke-width="1.6"/><circle cx="8" cy="6.5" r="2.2" fill="#fff"/><path d="M4 12.5c1-2 2.4-2.8 4-2.8s3 .8 4 2.8" fill="#fff"/></svg>User</li>
    </ul>
  </aside>

  <div class="panel order-form">
    <span class="lbl" style="left:32px;top:35px">Order No</span><span class="fld" style="left:125px;top:35px;width:126px">9670363</span>
    <span class="lbl" style="left:268px;top:35px">Reference</span><span class="fld" style="left:361px;top:35px;width:124px">9670363</span>
    <span class="lbl" style="left:504px;top:35px">Surname</span><span class="fld" style="left:595px;top:35px;width:126px">Order</span>
    <span class="fld" style="left:595px;top:74px;width:126px">0</span>
    <span class="fld" style="left:595px;top:113px;width:126px">0</span>
    <span class="fld" style="left:595px;top:151px;width:126px"></span>
    <span class="fld" style="left:595px;top:190px;width:126px">0</span>
    <span class="fld" style="left:595px;top:228px;width:126px">21/01/2022&nbsp; 02.55pm</span>
  </div>
  <div class="panel" style="top:480px;height:508px">
    <div class="select" style="top:43px"><svg width="10" height="6" viewBox="0 0 10 6"><path d="M1 1l4 4 4-4" fill="none" stroke="#79b5c9" stroke-width="1.3"/></svg></div>
    <div class="tray" style="top:99px;height:363px">
      <div class="tbl-wrap" style="top:29px;height:51px;background:var(--navy)"></div>
      <div class="scroll" style="left:665px;top:80px;height:256px"><i style="top:1px"></i><i style="bottom:1px"></i></div>
    </div>
  </div>

  <footer class="footer">© 2022 <b>TAILORFLOW</b> | &nbsp;All Rights Reserved<span class="code">C45</span></footer>

  <div class="shade"></div>

  <div class="modal" role="dialog" aria-label="Address">
    <div class="modal-head">ADDRESS<svg width="16" height="16" viewBox="0 0 16 16"><circle cx="8" cy="8" r="6.5" fill="none" stroke="#fff" stroke-width="1.5"/><path d="M5.5 5.5l5 5M10.5 5.5l-5 5" stroke="#fff" stroke-width="1.5"/></svg></div>

    <span class="mlbl" style="left:44px;top:100px">First Name</span><span class="mfld" style="left:44px;top:123px;width:250px">Test</span>
    <span class="mlbl" style="left:300px;top:100px">Surname</span><span class="mfld" style="left:300px;top:123px;width:250px">Order</span>
    <span class="mlbl" style="left:556px;top:100px">Attention Of</span><span class="mfld" style="left:556px;top:123px;width:250px">Fill Now</span>
    <span class="mlbl" style="left:44px;top:173px">Email</span><span class="mfld" style="left:44px;top:196px;width:250px">Your Email</span>
    <span class="mlbl" style="left:300px;top:173px">Phone</span><span class="mfld" style="left:300px;top:196px;width:250px">Your Phone</span>
    <span class="mlbl" style="left:556px;top:173px">Suburb</span><span class="mfld" style="left:556px;top:196px;width:250px">Fill Now</span>
    <span class="mlbl" style="left:44px;top:246px">Address 1</span><span class="mfld" style="left:44px;top:269px;width:762px">Your Address</span>
    <span class="mlbl" style="left:44px;top:319px">Address 2</span><span class="mfld" style="left:44px;top:342px;width:762px">Your Address</span>
    <span class="mlbl" style="left:44px;top:392px">City</span><span class="mfld" style="left:44px;top:415px;width:762px">Your City</span>
    <span class="mlbl" style="left:44px;top:465px">State</span><span class="mfld" style="left:44px;top:488px;width:762px">Your State</span>
    <span class="mlbl" style="left:44px;top:538px">Postcode</span><span class="mfld" style="left:44px;top:561px;width:762px">Your Postcode</span>
    <span class="mlbl" style="left:44px;top:611px">Country</span><span class="mfld" style="left:44px;top:634px;width:762px">Your Country</span>

    <div class="btn btn-outline" style="left:316px;top:688px;width:104px;height:39px">UBDATE</div>
    <div class="btn btn-fill" style="left:429px;top:688px;width:107px;height:39px;box-shadow:0 2px 4px rgba(0,0,0,.2)">CANCEL</div>
  </div>
</section>

</body>
</html>
```